Complete redesign of Licensed Medical Cannabis Dispensary website

Redesign website to modernize it and simplify it and add a self service reservation/preorder interactive delivery form. Also integrate current POS system that has current inventory. Here is a website for inspiration that I really like because of it simplicity https://www.grovaleaf.example and easy ordering option. Attached is our logo.... please design around that and this is our website address www.mistrelcourierhouse.example

Font styles to use
Sans Serif

Colors
5c5c5c
cbcbcb
000000
add136

Requirements
Must have
• inventory thats integrated with pos
• online reservation/delivery form
Nice to have
• a website thats modern and simple
• The website designed are the logo that is attached
Should not have
• too much information

```html
<!DOCTYPE html>
<html lang="en">
<head>
<meta charset="utf-8">
<title>Mistrel Courier House — Medical Marijuana Delivery</title>
<link href="https://fonts.googleapis.com/css2?family=Montserrat:wght@500;600;700&family=Lato:ital,wght@0,400;0,700;1,400&display=swap" rel="stylesheet">
<style>
:root{
  --green:#add136;
  --ink:#000000;
  --text:#5c5c5c;
  --line:#cbcbcb;
  --dark:#222222;
  --soft:#f4f4f4;
  --white:#ffffff;
}
*{box-sizing:border-box;margin:0;padding:0}
html,body{width:1200px;height:3636px;overflow:hidden}
body{font-family:"Lato",Arial,sans-serif;color:var(--ink);background:var(--white);position:relative}
.abs{position:absolute}
.btn{position:absolute;display:flex;align-items:center;justify-content:center;font-family:"Lato",sans-serif;font-size:17px;color:var(--white);background:var(--dark)}
.btn.green{background:var(--green);color:var(--ink)}

/* header */
.site-header{position:absolute;left:0;top:0;width:1200px;height:116px;background:var(--white)}
.brand{position:absolute;left:102px;top:36px;display:flex;align-items:center;gap:12px}
.brand-dot{width:42px;height:42px;border-radius:50%;background:var(--green)}
.brand-name{font-family:"Lato",sans-serif;font-size:20px;font-weight:400;color:var(--dark);white-space:nowrap}
.nav a{position:absolute;top:46px;font-family:"Montserrat",sans-serif;font-weight:500;font-size:15px;color:var(--ink);text-decoration:none}
.icon-circle{position:absolute;width:38px;height:38px;border-radius:50%;background:var(--green);display:flex;align-items:center;justify-content:center}

/* hero */
.hero{position:absolute;left:0;top:116px;width:1200px;height:514px;background:linear-gradient(180deg,#ececec,#dddddd)}
.hero-photo{position:absolute;left:0;top:30px;width:700px;height:484px;background:radial-gradient(ellipse at 40% 60%,#6b3f1e 0%,#8a5a2c 25%,#6f9b3a 50%,rgba(221,221,221,0) 75%)}
.hero h1{position:absolute;left:686px;top:100px;font-family:"Montserrat",sans-serif;font-weight:700;color:var(--green);font-size:40px;line-height:48px}
.hero p{position:absolute;left:686px;top:210px;width:440px;font-size:17px;line-height:28px;color:var(--dark)}
.dots{position:absolute;left:686px;top:378px;display:flex;gap:6px}
.dots span{width:15px;height:15px;border-radius:50%;background:#999}
.dots span:first-child{background:var(--dark)}

/* band */
.promo{position:absolute;left:0;top:630px;width:1200px;height:78px;background:var(--green)}
.promo p{position:absolute;left:98px;top:27px;font-size:19px;color:var(--white)}

/* features */
.feature{position:absolute;top:796px;width:300px;text-align:center}
.feature-ring{margin:0 auto;width:212px;height:212px;border-radius:50%;border:4px solid var(--green);display:flex;align-items:center;justify-content:center}
.feature-core{width:186px;height:186px;border-radius:50%;background:var(--green);display:flex;align-items:center;justify-content:center}
.feature h3{margin-top:32px;font-family:"Montserrat",sans-serif;font-weight:700;font-size:22px;letter-spacing:.5px}
.feature p{margin:14px auto 0;width:270px;font-size:15px;line-height:23px;color:var(--dark)}

/* product sections */
.section-title{position:absolute;left:0;width:1200px;text-align:center;font-family:"Montserrat",sans-serif;font-weight:700;font-size:27px;color:var(--green)}
.title-rule{position:absolute;left:572px;width:56px;height:3px;background:var(--green)}
.title-rule.white{background:var(--white)}
.flowers{position:absolute;left:0;top:1217px;width:1200px;height:572px;background:var(--soft)}
.product{position:absolute;width:260px;text-align:center}
.product-photo{margin:0 auto;width:184px;height:184px;border-radius:50%}
.product h4{margin-top:20px;font-weight:400;font-size:16px;color:var(--dark);white-space:nowrap}
.price{margin-top:6px;font-family:"Montserrat",sans-serif;font-weight:700;font-size:24px;color:var(--green)}

/* testimonials */
.testimonials{position:absolute;left:0;top:2349px;width:1200px;height:490px;background:linear-gradient(180deg,#1a1a14,#3b4a2a 45%,#2a2a20)}
.testimonials h2{position:absolute;left:0;top:60px;width:1200px;text-align:center;font-family:"Montserrat",sans-serif;font-weight:700;font-size:27px;color:var(--white)}
.avatar{position:absolute;left:549px;top:174px;width:102px;height:102px;border-radius:50%;border:3px solid var(--white);background:#6a5242}
.quote{position:absolute;left:280px;top:300px;width:640px;text-align:center;font-style:italic;font-size:23px;line-height:38px;color:var(--white)}
.author{position:absolute;left:0;top:396px;width:1200px;text-align:center;font-family:"Montserrat",sans-serif;font-weight:600;font-size:17px;color:var(--white)}
.arrow{position:absolute;top:226px}

/* reservation */
.reserve{position:absolute;left:0;top:2839px;width:1200px;height:397px;background:var(--green)}
.reserve h2{position:absolute;left:0;top:44px;width:1200px;text-align:center;font-family:"Montserrat",sans-serif;font-weight:700;font-size:27px;color:var(--white)}
.field{position:absolute;height:48px;border:2px solid var(--white);padding-left:14px;display:flex;align-items:center;font-size:17px;color:var(--white)}

/* footer */
.site-footer{position:absolute;left:0;top:3236px;width:1200px;height:400px;background:var(--white)}
.footer-col{position:absolute;top:86px}
.footer-col h5{font-family:"Montserrat",sans-serif;font-weight:700;font-size:19px;letter-spacing:.5px;margin-bottom:16px}
.footer-col li{list-style:none;display:flex;gap:10px;font-size:15px;line-height:29px;color:var(--dark)}
.footer-col li svg{flex:none;margin-top:9px}
.footer-rule{position:absolute;left:100px;top:335px;width:1000px;height:1px;background:var(--line)}
.copyright{position:absolute;left:0;top:358px;width:1200px;text-align:center;font-size:15px;color:var(--dark)}
</style>
</head>
<body>

<header class="site-header">
  <div class="brand"><span class="brand-dot"></span><span class="brand-name">Mistrel Courier House</span></div>
  <nav class="nav">
    <a style="left:407px">LOGIN/SIGN UP</a>
    <a style="left:555px">CONTACT</a>
    <a style="left:657px">FORUMS</a>
    <a style="left:754px">STORE</a>
  </nav>
  <div class="icon-circle" style="left:823px;top:36px">
    <svg width="18" height="18" viewBox="0 0 24 24"><path fill="#fff" d="M6.6 10.8a15.1 15.1 0 0 0 6.6 6.6l2.2-2.2a1 1 0 0 1 1-.25 11.4 11.4 0 0 0 3.6.6 1 1 0 0 1 1 1V20a1 1 0 0 1-1 1A17 17 0 0 1 3 4a1 1 0 0 1 1-1h3.5a1 1 0 0 1 1 1c0 1.25.2 2.45.6 3.6a1 1 0 0 1-.25 1z"/></svg>
  </div>
  <a class="abs" style="left:870px;top:46px;font-family:'Montserrat',sans-serif;font-weight:500;font-size:15px;color:#000;text-decoration:none">ORDERS: 555-014-2290</a>
  <div class="icon-circle" style="left:1063px;top:36px">
    <svg width="18" height="18" viewBox="0 0 24 24"><path fill="#fff" d="M2 3h3l2.7 11h10.6L21 6H7.2L6.6 4H2zM9 17.5a1.8 1.8 0 1 0 0 3.6 1.8 1.8 0 0 0 0-3.6zm8 0a1.8 1.8 0 1 0 0 3.6 1.8 1.8 0 0 0 0-3.6z"/></svg>
  </div>
</header>

<section class="hero">
  <div class="hero-photo" role="img" aria-label="Amber tincture bottles, jars, a cannabis leaf and dried flower"></div>
  <h1>TOP SHELF MEDICAL<br>Marijuana Delivery</h1>
  <p>We offer only the highest quality flowers, edibles and concentrates.</p>
  <div class="btn green" style="left:686px;top:290px;width:109px;height:46px">Shop Now</div>
  <div class="btn" style="left:806px;top:290px;width:119px;height:46px">Get Certified</div>
  <div class="dots"><span></span><span></span><span></span><span></span></div>
</section>

<section class="promo">
  <p>Don't have your doctor's recommendation yet? Get it online for just $49!</p>
  <div class="btn" style="left:798px;top:16px;width:118px;height:46px">Get Started</div>
</section>

<section class="features">
  <div class="feature" style="left:100px">
    <div class="feature-ring"><div class="feature-core">
      <svg width="66" height="80" viewBox="0 0 66 80" fill="none" stroke="#fff" stroke-width="4"><path d="M4 4h40l18 18v54H4z"/><path d="M44 4v18h18M16 38h34M16 50h34M16 62h34"/></svg>
    </div></div>
    <h3>GET VERIFIED</h3>
    <p>It's fast. It's simple. Just fill out our verification form and get approved in minutes.</p>
  </div>
  <div class="feature" style="left:456px">
    <div class="feature-ring"><div class="feature-core">
      <svg width="86" height="76" viewBox="0 0 86 76" fill="none" stroke="#fff" stroke-width="4"><path d="M2 6h14l10 42h46l10-32H22"/><path d="M34 26v14M48 26v14M62 26v14"/><circle cx="32" cy="64" r="6"/><circle cx="66" cy="64" r="6"/></svg>
    </div></div>
    <h3>SHOP</h3>
    <p>Add the products you want to your shopping cart and check out. No credit card required!</p>
  </div>
  <div class="feature" style="left:808px">
    <div class="feature-ring"><div class="feature-core">
      <svg width="80" height="80" viewBox="0 0 80 80" fill="none" stroke="#fff" stroke-width="4"><circle cx="40" cy="40" r="36"/><path d="M24 41l11 11 22-24"/></svg>
    </div></div>
    <h3>GET MEDICATED</h3>
    <p>Sit back and wait. Our professional staff will deliver your medication right to your front door.</p>
  </div>
</section>

<section class="flowers">
  <h2 class="section-title" style="top:52px">FLOWERS</h2>
  <div class="title-rule" style="top:101px"></div>
  <div class="product" style="left:83px;top:162px">
    <div class="product-photo" role="img" aria-label="Harbor Mist dried flower" style="background:radial-gradient(circle,#8a8a7a,#4c4d44)"></div>
    <h4>Harbor Mist (Private Reserve)</h4><div class="price">15.00 - 60.00</div>
  </div>
  <div class="product" style="left:340px;top:162px">
    <div class="product-photo" role="img" aria-label="Tree Sap #4 dried flower" style="background:radial-gradient(circle,#c9a95a,#5a4a28)"></div>
    <h4>Tree Sap #4</h4><div class="price">15.00 - 60.00</div>
  </div>
  <div class="product" style="left:600px;top:162px">
    <div class="product-photo" role="img" aria-label="Preroll" style="background:radial-gradient(circle,#8d9458,#3b3d26)"></div>
    <h4>Preroll</h4><div class="price">15.00 - 60.00</div>
  </div>
  <div class="product" style="left:857px;top:162px">
    <div class="product-photo" role="img" aria-label="Sugar Meadow dried flower" style="background:radial-gradient(circle,#b09a6a,#5e4d33)"></div>
    <h4>Sugar Meadow</h4><div class="price">15.00 - 60.00</div>
  </div>
  <div class="btn green" style="left:161px;top:446px;width:104px;height:46px">Buy Now</div>
  <div class="btn" style="left:418px;top:446px;width:104px;height:46px">Buy Now</div>
  <div class="btn" style="left:678px;top:446px;width:104px;height:46px">Buy Now</div>
  <div class="btn" style="left:935px;top:446px;width:104px;height:46px">Buy Now</div>
</section>

<section class="concentrates">
  <h2 class="section-title" style="top:1859px">CONCENTRATE</h2>
  <div class="title-rule" style="top:1908px"></div>
  <div class="product" style="left:83px;top:1968px">
    <div class="product-photo" role="img" aria-label="Velvet Tone Live Resin in a glass jar" style="background:radial-gradient(circle,#6b4a22,#bfbfbf 70%)"></div>
    <h4>Velvet Tone Live Resin</h4>
  </div>
  <div class="product" style="left:340px;top:1968px">
    <div class="product-photo" role="img" aria-label="Orchard Glow Shatter" style="background:radial-gradient(circle,#6a4a2c,#c9c5bd 70%)"></div>
    <h4>Orchard Glow Shatter</h4>
  </div>
  <div class="product" style="left:600px;top:1968px">
    <div class="product-photo" role="img" aria-label="Marlow's Budder in a jar" style="background:radial-gradient(circle,#d69a2e,#3a3a3a 75%)"></div>
    <h4>Marlow's Budder</h4>
  </div>
  <div class="product" style="left:857px;top:1968px">
    <div class="product-photo" role="img" aria-label="Live Resin Budder Coastline Reserve" style="background:radial-gradient(circle,#e0a63a,#4a3a22 80%)"></div>
    <h4>Live Resin Budder Coastline Reserve</h4>
  </div>
  <div class="btn green" style="left:161px;top:2220px;width:104px;height:44px">Buy Now</div>
  <div class="btn" style="left:418px;top:2220px;width:104px;height:44px">Buy Now</div>
  <div class="btn" style="left:678px;top:2220px;width:104px;height:44px">Buy Now</div>
  <div class="btn" style="left:935px;top:2220px;width:104px;height:44px">Buy Now</div>
</section>

<section class="testimonials" role="img" aria-label="Dried cannabis flower spilling from a jar on a wooden table">
  <h2>OUR TESTIMONIALS</h2>
  <div class="title-rule white" style="top:110px"></div>
  <div class="avatar" role="img" aria-label="Customer portrait"></div>
  <p class="quote">"These guys really know their stuff man. Nothin' but the kind here!"</p>
  <p class="author">- DALE R.</p>
  <svg class="arrow" style="left:42px" width="22" height="40" viewBox="0 0 22 40"><path d="M20 2 3 20l17 18" fill="none" stroke="#fff" stroke-width="3"/></svg>
  <svg class="arrow" style="left:1136px" width="22" height="40" viewBox="0 0 22 40"><path d="M2 2l17 18L2 38" fill="none" stroke="#fff" stroke-width="3"/></svg>
</section>

<section class="reserve">
  <h2>ONLINE RESERVATION</h2>
  <div class="title-rule white" style="top:96px"></div>
  <div class="field" style="left:104px;top:150px;width:323px">Name</div>
  <div class="field" style="left:439px;top:150px;width:322px">Email</div>
  <div class="field" style="left:771px;top:150px;width:322px">Phone Number</div>
  <div class="field" style="left:104px;top:210px;width:989px">Concentrate
    <svg class="abs" style="right:18px;top:19px" width="12" height="8" viewBox="0 0 12 8"><path d="M0 0h12L6 8z" fill="#fff"/></svg>
  </div>
  <div class="btn" style="left:528px;top:288px;width:143px;height:48px;font-weight:700">Book Now</div>
</section>

<footer class="site-footer">
  <div class="brand" style="left:102px;top:174px"><span class="brand-dot"></span><span class="brand-name">Mistrel Courier House</span></div>
  <div class="footer-col" style="left:422px">
    <h5>EXPLORE</h5>
    <ul>
      <li><svg width="12" height="10" viewBox="0 0 12 10"><path d="M0 5h10M6 1l4 4-4 4" fill="none" stroke="#222" stroke-width="1.6"/></svg>Store</li>
      <li><svg width="12" height="10" viewBox="0 0 12 10"><path d="M0 5h10M6 1l4 4-4 4" fill="none" stroke="#222" stroke-width="1.6"/></svg>Cart</li>
      <li><svg width="12" height="10" viewBox="0 0 12 10"><path d="M0 5h10M6 1l4 4-4 4" fill="none" stroke="#222" stroke-width="1.6"/></svg>My Account</li>
      <li><svg width="12" height="10" viewBox="0 0 12 10"><path d="M0 5h10M6 1l4 4-4 4" fill="none" stroke="#222" stroke-width="1.6"/></svg>New Patient Verification</li>
      <li><svg width="12" height="10" viewBox="0 0 12 10"><path d="M0 5h10M6 1l4 4-4 4" fill="none" stroke="#222" stroke-width="1.6"/></svg>Contact Us</li>
    </ul>
  </div>
  <div class="footer-col" style="left:679px;width:230px">
    <h5>FORUMS</h5>
    <ul>
      <li><svg width="12" height="10" viewBox="0 0 12 10"><path d="M0 5h10M6 1l4 4-4 4" fill="none" stroke="#222" stroke-width="1.6"/></svg>Bongs, Bubblers, &amp; Water Pipes</li>
      <li><svg width="12" height="10" viewBox="0 0 12 10"><path d="M0 5h10M6 1l4 4-4 4" fill="none" stroke="#222" stroke-width="1.6"/></svg>Concentrates</li>
      <li><svg width="12" height="10" viewBox="0 0 12 10"><path d="M0 5h10M6 1l4 4-4 4" fill="none" stroke="#222" stroke-width="1.6"/></svg>Growing</li>
      <li><svg width="12" height="10" viewBox="0 0 12 10"><path d="M0 5h10M6 1l4 4-4 4" fill="none" stroke="#222" stroke-width="1.6"/></svg>Vaporizers</li>
      <li><svg width="12" height="10" viewBox="0 0 12 10"><path d="M0 5h10M6 1l4 4-4 4" fill="none" stroke="#222" stroke-width="1.6"/></svg>What Are You Smokin'?</li>
    </ul>
  </div>
  <div class="footer-col" style="left:936px">
    <h5>RECENT TOPICS</h5>
    <ul>
      <li><svg width="12" height="10" viewBox="0 0 12 10"><path d="M0 5h10M6 1l4 4-4 4" fill="none" stroke="#222" stroke-width="1.6"/></svg>Glass or metal?</li>
      <li><svg width="12" height="10" viewBox="0 0 12 10"><path d="M0 5h10M6 1l4 4-4 4" fill="none" stroke="#222" stroke-width="1.6"/></svg>Sexing your plant</li>
    </ul>
  </div>
  <div class="footer-rule"></div>
  <p class="copyright">Copyrights @ 2018 Mistrel Courier House Delivery. All Rights Reserved.</p>
</footer>

</body>
</html>
```